Corporate Christmas Hamper Guide 2021

We are an online Hamper business in Australia and we need to design and produce our Christmas Hamper brochure for this year. It will need to be a pdf format which will become a digital online brochure. Our business Bramblewood Baskets (www.bramblewoodbaskets.com.au) is a website that curates, packages and delivers hampers for both consumers and corporates. This specific brochure is targetted to the business market. The person who will review the brochure will generally be Executive assistants, Personal Assistants, Marketing Directors and their staff, Senior Managers as well as small business owners. Primaily they will be women.

Hampers are a luxury gift and Christmas is a traditional time for businesses to give their staff, clients, special customers and suppliers a gift to say thankyou for their support over the year. With Covid, this year has made it more difficult to stay connected to colleagues and clients and a hamper is a great way to do that so we anticipate it will be very popular this year.

I have attached our brochure from last year which was a super quick job (not done by a designer). We had recently purchased the business and we just needed to get something out. This is very substandard but I send it to you to see the sorts of things we will include in the brochure.

This job entails intial design and layout then once agreed final production including free image sourcing (hamper photography will be provided but other stylistic and suitable lifestyle photography to enhance the brochure will need to be sourced by you....royalty free). a more detailed design brief is attached below.

```html
<!DOCTYPE html>
<html lang="en">
<head>
<meta charset="utf-8">
<title>Bramblewood Baskets – Corporate Christmas Hamper Guide 2021</title>
<link href="https://fonts.googleapis.com/css2?family=Oswald:wght@500;600&family=Open+Sans:wght@400;600;700&display=swap" rel="stylesheet">
<style>
:root{
  --red:#d0171d;
  --ink:#2a2a2a;
  --text:#4a4a4a;
  --footer:#2b2b2b;
  --canvas:#e9e9e9;
  --paper:#ffffff;
}
*{box-sizing:border-box;margin:0;padding:0}
html,body{width:1200px;height:4926px;overflow:hidden}
body{background:var(--canvas);font-family:"Open Sans",sans-serif;color:var(--text);position:relative}
.page{position:absolute;width:530px;height:750px;background:var(--paper);overflow:hidden;box-shadow:0 1px 4px rgba(0,0,0,.12)}
.col-l{left:42px}.col-r{left:626px}.col-c{left:334px}
.row1{top:76px}.row2{top:862px}.row3{top:1656px}.row4{top:2452px}.row5{top:3254px}.row6{top:4058px}

.band{position:absolute;left:0;right:0;top:24px;height:36px;background:var(--red);color:#fff;
  font-family:"Oswald",sans-serif;font-weight:500;font-size:21px;letter-spacing:.5px;text-align:center;line-height:36px}
.items{position:absolute;left:24px;right:24px;top:74px;bottom:44px;display:flex;flex-direction:column;justify-content:space-between}
.item{display:flex;gap:18px;align-items:flex-start;height:205px;overflow:hidden}
.item.flip{flex-direction:row-reverse}
.item-copy{flex:1;min-width:0}
.item-head{display:flex;justify-content:space-between;align-items:flex-start;gap:8px;margin-bottom:6px}
.item-name{color:var(--red);font-weight:700;font-size:14px;line-height:1.2}
.price{background:var(--red);color:#fff;font-weight:700;font-size:15px;padding:1px 8px;white-space:nowrap}
.item-desc{font-size:10.4px;line-height:1.38;text-align:justify}
.photo{width:226px;height:170px;flex:none;border-radius:2px}
.ph-red{background:linear-gradient(135deg,#f4eeee,#e7c9c6 55%,#b8322f)}
.ph-gold{background:linear-gradient(135deg,#f5efe6,#d9c29a 55%,#7b5a34)}
.ph-dark{background:linear-gradient(135deg,#f1f1f1,#9c9c9c 55%,#2b2b2b)}
.ph-green{background:linear-gradient(135deg,#f2f4f1,#b9c7b4 55%,#3f5a45)}
.wine-list{font-size:10.4px;line-height:1.4;margin-top:4px}
.wine-list li{list-style:none;display:flex;justify-content:space-between}
.wine-list b{display:block;color:var(--ink);margin-bottom:2px}

.footer{position:absolute;left:0;right:0;bottom:0;height:34px;background:var(--footer);color:#fff;
  display:flex;align-items:center;justify-content:space-around;font-size:10px;padding:0 10px}
.footer span{display:flex;align-items:center;gap:6px}
.footer svg{width:16px;height:16px}

.brand{font-weight:700;font-size:30px;color:var(--ink);text-align:center;line-height:1;letter-spacing:-.5px}
.cover .brand{position:absolute;top:44px;left:0;right:0}
.cover-title{position:absolute;top:118px;left:0;right:0;height:110px;background:var(--red);color:#fff;
  font-family:"Oswald",sans-serif;font-weight:600;font-size:36px;line-height:44px;text-align:center;padding-top:12px}
.cover-photo{position:absolute;top:228px;left:0;right:0;bottom:34px;
  background:radial-gradient(ellipse at 50% 45%,#e7a55c 0,#c56b35 35%,#6e3a22 70%,#3a2217 100%)}

.intro{background:linear-gradient(180deg,#fafafa,#eeeeee 70%,#ffffff)}
.intro .brand{position:absolute;top:36px;left:0;right:0}
.intro-panel{position:absolute;top:110px;left:40px;right:40px;background:rgba(255,255,255,.7);padding:14px 16px;
  font-size:10.6px;line-height:1.4;text-align:center;color:var(--ink)}
.intro-panel p{margin-bottom:10px}
.intro-panel small{font-size:8.5px;display:block}
.earlybird{position:absolute;top:440px;left:60px;right:60px;text-align:center;font-size:10.6px;line-height:1.4;color:var(--ink)}
.earlybird h3{font-size:14px;margin-bottom:4px}
.intro-photo{position:absolute;left:0;right:0;bottom:34px;height:170px;
  background:linear-gradient(180deg,rgba(255,255,255,0),#e9e3e3 35%,#c73a3a 80%,#9a1f22)}

.includes{position:absolute;left:24px;right:24px;top:530px;font-size:10px;line-height:1.4;text-align:justify}
.includes b{color:var(--ink)}

.order{background:linear-gradient(135deg,#e4dccb,#cfc2a3 50%,#e8e1d2)}
.sheet{position:absolute;left:22px;right:22px;top:22px;bottom:56px;background:rgba(255,255,255,.88);padding:18px 22px}
.sheet h3{color:var(--red);font-size:14px;margin:0 0 6px}
.sheet p,.sheet li{font-size:9.6px;line-height:1.4}
.sheet ul{padding-left:14px;margin-bottom:4px}
.sheet li{list-style:none;position:relative}
.sheet li::before{content:"";position:absolute;left:-11px;top:5px;width:5px;height:5px;border-radius:50%;background:var(--red)}
.sheet section{margin-bottom:16px}
.quote{border-top:1px solid var(--red);border-bottom:1px solid var(--red);padding:8px 4px;margin:10px 0;font-style:italic;font-size:9.6px;line-height:1.4}
.quote cite{display:block;text-align:right;font-weight:600;color:var(--ink)}

.custom{background:linear-gradient(135deg,#f7f7f7,#e8e8e8)}
.custom .sheet{bottom:50px}
.split{display:flex;gap:14px;margin-bottom:16px}
.split>div{flex:1}
.split .photo{width:210px;height:150px}
.suppliers{display:grid;grid-template-columns:repeat(4,1fr);gap:10px;margin-top:10px;padding:0 10px}
.badge{height:42px;background:#fff;border:1px solid #d9d9d9}
.badge.last{grid-column:2/4}
</style>
</head>
<body>

<!-- Cover -->
<article class="page col-l row1 cover">
  <div class="brand">Bramblewood Baskets</div>
  <h1 class="cover-title">CORPORATE CHRISTMAS<br>HAMPER GUIDE 2021</h1>
  <div class="cover-photo" role="img" aria-label="Christmas tree stacked from wrapped gift boxes with a Santa hat on a wooden table"></div>
  <footer class="footer">
    <span><svg viewBox="0 0 16 16"><circle cx="8" cy="8" r="7" fill="none" stroke="#fff"/><path d="M5.5 4.5l1.5 1.6-.8 1c.6 1.2 1.4 2 2.6 2.6l1-.8 1.6 1.5-.9 1.1C7.8 11.3 4.9 8.4 4.4 5.4z" fill="#fff"/></svg>1300 41 27 90</span>
    <span><svg viewBox="0 0 16 16"><circle cx="8" cy="8" r="7" fill="none" stroke="#fff"/><rect x="4.5" y="5.5" width="7" height="5" fill="none" stroke="#fff"/><path d="M4.5 5.5l3.5 3 3.5-3" fill="none" stroke="#fff"/></svg>corporate@bramblewoodbaskets.com.au</span>
    <span><svg viewBox="0 0 16 16"><circle cx="8" cy="8" r="7" fill="none" stroke="#fff"/><circle cx="8" cy="8" r="3.5" fill="none" stroke="#fff"/><path d="M4.5 8h7M8 4.5v7" stroke="#fff"/></svg>www.bramblewoodbaskets.com.au</span>
  </footer>
</article>

<!-- Intro -->
<article class="page col-r row1 intro">
  <div class="brand">Bramblewood Baskets</div>
  <div class="intro-panel">
    <p>Show your clients how much you appreciate them this Christmas! And what better way to express your gratitude than by sending them a beautiful handpacked hamper from the team at Bramblewood Baskets.</p>
    <p>We will deliver your corporate gifts anywhere around Australia with FREE Standard Shipping. Or for an additional cost of just $9.95 per hamper there is the Premium service of 1 - 2 Business Day delivery.</p>
    <p>Why not tailor your gifts with a free gift card and customised ribbon with your business logo, for maximum brand impact.</p>
    <p>Quality assured, handpicked and taste-tested by our friends, family and staff; the artisan, luxury and award-winning brands we house here at Bramblewood Baskets are a genuine pleasure to share.</p>
    <small>*Some hamper items may be substituted due to stock availability at this busy time.</small>
  </div>
  <div class="earlybird">
    <h3>Early Bird Special</h3>
    <p>Receive 5% OFF when you order 10 or more hampers and pay by 13 November. Simply complete our Bulk Order Form and email to corporate@bramblewoodbaskets.com.au and we will apply the discount to your final invoice.*Discount does not apply to shipping*</p>
  </div>
  <div class="intro-photo" role="img" aria-label="Red and white Christmas baubles resting in soft snow"></div>
  <footer class="footer">
    <span><svg viewBox="0 0 16 16"><circle cx="8" cy="8" r="7" fill="none" stroke="#fff"/><path d="M5.5 4.5l1.5 1.6-.8 1c.6 1.2 1.4 2 2.6 2.6l1-.8 1.6 1.5-.9 1.1C7.8 11.3 4.9 8.4 4.4 5.4z" fill="#fff"/></svg>1300 41 27 90</span>
    <span><svg viewBox="0 0 16 16"><circle cx="8" cy="8" r="7" fill="none" stroke="#fff"/><rect x="4.5" y="5.5" width="7" height="5" fill="none" stroke="#fff"/><path d="M4.5 5.5l3.5 3 3.5-3" fill="none" stroke="#fff"/></svg>corporate@bramblewoodbaskets.com.au</span>
    <span><svg viewBox="0 0 16 16"><circle cx="8" cy="8" r="7" fill="none" stroke="#fff"/><circle cx="8" cy="8" r="3.5" fill="none" stroke="#fff"/><path d="M4.5 8h7M8 4.5v7" stroke="#fff"/></svg>www.bramblewoodbaskets.com.au</span>
  </footer>
</article>

<!-- Under $100 -->
<article class="page col-l row2">
  <h2 class="band">UNDER $100</h2>
  <div class="items">
    <div class="item">
      <div class="item-copy">
        <div class="item-head"><h3 class="item-name">Tempting Treats</h3><span class="price">$75</span></div>
        <p class="item-desc">Here's a bit of all things tempting! This corporate best seller is packed full of goodies for its lucky recipients. Includes our mouth-watering Pretzels, Beer Nuts, Shortbread Bites, Crackerthins, Soft Jubes, Choc fruit and nuts and Crispy Chocolate Coconut Rolls.</p>
      </div>
      <div class="photo ph-red" role="img" aria-label="Hamper box of snacks and sweets"></div>
    </div>
    <div class="item flip">
      <div class="item-copy">
        <div class="item-head"><h3 class="item-name">Feeling Peckish</h3><span class="price">$89</span></div>
        <p class="item-desc">Snack Attack? A great share pack for the whole team. Chock full of tasty sweet and savoury treats including Crispin Co Chipotle and Lime Tortilla Chips, Salted Pretzels, Caramel Covered Popcorn, Pippa's Handmade Double Choc Chip Bites, Handmade Chocolate Roadblock, Beer Nuts and Soft Jubes.</p>
      </div>
      <div class="photo ph-gold" role="img" aria-label="Share pack of chips, popcorn and chocolate treats"></div>
    </div>
    <div class="item">
      <div class="item-copy">
        <div class="item-head"><h3 class="item-name">Luxury Wine Case<br>&amp; Wine of Choice</h3><span class="price">$35+wine</span></div>
        <ul class="wine-list">
          <b>Choose from</b>
          <li><span>Jonah Q Sauvignon Blanc</span><span>+$25</span></li>
          <li><span>Halden Pinot Noir</span><span>+$25</span></li>
          <li><span>Kauri Bay Rosé</span><span>+$30</span></li>
          <li><span>Ridgeway Cabernet Merlot</span><span>+$40</span></li>
          <li><span>Cape Lindell Shiraz</span><span>+$65</span></li>
        </ul>
        <p class="item-desc" style="margin-top:5px">A simple yet sophisticated corporate gift. Choose from 5 different wines, presented in a mock-leather wine case which includes a bottle opener, a pouring spout, drip-stop ring and foil cutter.</p>
      </div>
      <div class="photo ph-dark" role="img" aria-label="Black leather wine case holding a bottle and accessories"></div>
    </div>
  </div>
  <footer class="footer">
    <span><svg viewBox="0 0 16 16"><circle cx="8" cy="8" r="7" fill="none" stroke="#fff"/><path d="M5.5 4.5l1.5 1.6-.8 1c.6 1.2 1.4 2 2.6 2.6l1-.8 1.6 1.5-.9 1.1C7.8 11.3 4.9 8.4 4.4 5.4z" fill="#fff"/></svg>1300 41 27 90</span>
    <span><svg viewBox="0 0 16 16"><circle cx="8" cy="8" r="7" fill="none" stroke="#fff"/><rect x="4.5" y="5.5" width="7" height="5" fill="none" stroke="#fff"/><path d="M4.5 5.5l3.5 3 3.5-3" fill="none" stroke="#fff"/></svg>corporate@bramblewoodbaskets.com.au</span>
    <span><svg viewBox="0 0 16 16"><circle cx="8" cy="8" r="7" fill="none" stroke="#fff"/><circle cx="8" cy="8" r="3.5" fill="none" stroke="#fff"/><path d="M4.5 8h7M8 4.5v7" stroke="#fff"/></svg>www.bramblewoodbaskets.com.au</span>
  </footer>
</article>

<!-- Under $120 -->
<article class="page col-r row2">
  <h2 class="band">UNDER $120</h2>
  <div class="items">
    <div class="item">
      <div class="item-copy">
        <div class="item-head"><h3 class="item-name">Indulge Her</h3><span class="price">$89</span></div>
        <p class="item-desc">A touch of indulgence so beautifully presented, making a stunning statement of thanks. Lune Botanica Royal Frangipani Botanical candle, Bloomhaus luxury handcream and a fun Speckletop Christmas treat. What more can a girl want!. A gift of gratitude and thanks.</p>
      </div>
      <div class="photo ph-red" role="img" aria-label="Gift box with candle, handcream and Christmas treat"></div>
    </div>
    <div class="item flip">
      <div class="item-copy">
        <div class="item-head"><h3 class="item-name">Sweet Christmas Bites</h3><span class="price">$119</span></div>
        <p class="item-desc">Enjoy the tasty treats on offer with this gourmet gift hamper! Includes our selection of Chocolates from Hartwell Chocolatier &amp; Juniper &amp; Fig, Salted Caramel Sauce, a touch of Festive Fare with our Gingerbread Christmas Cookie, White Choc Christmas slice, Christmas Freckle and some sparkly additions for him and her from Lumiere Crystal Christmas Bon Bon's! (Contains 2 Bon Bons containing one set of; Necklace, Earrings, Tie Clip or Cufflinks)</p>
      </div>
      <div class="photo ph-gold" role="img" aria-label="Hamper of chocolates, caramel sauce and Christmas bon bons"></div>
    </div>
    <div class="item">
      <div class="item-copy">
        <div class="item-head"><h3 class="item-name">Green Thumb</h3><span class="price">$109</span></div>
        <p class="item-desc">Our best selling staff favourite is all about self care while enjoying the beautiful outdoors. Botanically inspired &amp; designed for hardworking Gardeners. Includes Fernlea Aroma's nourishing Wild Lime &amp; Mint SPF 15+ UVA and UVB protection hand cream, their gentle Therapy Garden Hand Wash, natural scented Citronella Candle and Hand Towel.</p>
      </div>
      <div class="photo ph-green" role="img" aria-label="Garden themed pamper set with hand cream, wash, candle and towel"></div>
    </div>
  </div>
  <footer class="footer">
    <span><svg viewBox="0 0 16 16"><circle cx="8" cy="8" r="7" fill="none" stroke="#fff"/><path d="M5.5 4.5l1.5 1.6-.8 1c.6 1.2 1.4 2 2.6 2.6l1-.8 1.6 1.5-.9 1.1C7.8 11.3 4.9 8.4 4.4 5.4z" fill="#fff"/></svg>1300 41 27 90</span>
    <span><svg viewBox="0 0 16 16"><circle cx="8" cy="8" r="7" fill="none" stroke="#fff"/><rect x="4.5" y="5.5" width="7" height="5" fill="none" stroke="#fff"/><path d="M4.5 5.5l3.5 3 3.5-3" fill="none" stroke="#fff"/></svg>corporate@bramblewoodbaskets.com.au</span>
    <span><svg viewBox="0 0 16 16"><circle cx="8" cy="8" r="7" fill="none" stroke="#fff"/><circle cx="8" cy="8" r="3.5" fill="none" stroke="#fff"/><path d="M4.5 8h7M8 4.5v7" stroke="#fff"/></svg>www.bramblewoodbaskets.com.au</span>
  </footer>
</article>

<!-- Under $160 -->
<article class="page col-l row3">
  <h2 class="band">UNDER $160</h2>
  <div class="items">
    <div class="item">
      <div class="item-copy">
        <div class="item-head"><h3 class="item-name">Whisky Delights</h3><span class="price">$149</span></div>
        <p class="item-desc">Och Aye. Keep it simple with Glenmorrow and Fruit Cake this Christmas. Hollowbrook Bakehouse Italian Style Gourmet Fruit &amp; Nut cake, coupled with a glass of whisky is sure to hit the spot. A great way to show thanks and gratitude to whisky lovers.</p>
      </div>
      <div class="photo ph-gold" role="img" aria-label="Whisky bottle beside a boxed fruit cake"></div>
    </div>
    <div class="item flip">
      <div class="item-copy">
        <div class="item-head"><h3 class="item-name">Beers for Christmas</h3><span class="price">$129</span></div>
        <p class="item-desc">You can't go wrong with this special gift hamper including a perfect pairing of Harbour Brewing beer and Orchard Row Co Nibbles 2 x Gourmet nuts, 2 x Crackerthins, Beef Jerky, Olives and 2 x condiments. Ideal for the beer connoisseur or when you just can't decide what gift to buy. A great hamper to share especially at Christmas time.</p>
      </div>
      <div class="photo ph-dark" role="img" aria-label="Box of craft beers with nibbles and condiments"></div>
    </div>
    <div class="item">
      <div class="item-copy">
        <div class="item-head"><h3 class="item-name">Cream and Berries</h3><span class="price">$139</span></div>
        <p class="item-desc">Everyone loves a Creamhollow and there's no better time than at Christmas. Our gourmet treats will all have a Berry theme ...Langues de Chat Raspberry Buttery Almond Snaps, Thimble Kitchen's Raspberry Meringues and the ever so Moorish Rocky Road. Topped off with a full size bottle of Creamhollow. All set for that after dinner Christmas tipple.</p>
      </div>
      <div class="photo ph-red" role="img" aria-label="Cream liqueur bottle with berry themed sweets"></div>
    </div>
  </div>
  <footer class="footer">
    <span><svg viewBox="0 0 16 16"><circle cx="8" cy="8" r="7" fill="none" stroke="#fff"/><path d="M5.5 4.5l1.5 1.6-.8 1c.6 1.2 1.4 2 2.6 2.6l1-.8 1.6 1.5-.9 1.1C7.8 11.3 4.9 8.4 4.4 5.4z" fill="#fff"/></svg>1300 41 27 90</span>
    <span><svg viewBox="0 0 16 16"><circle cx="8" cy="8" r="7" fill="none" stroke="#fff"/><rect x="4.5" y="5.5" width="7" height="5" fill="none" stroke="#fff"/><path d="M4.5 5.5l3.5 3 3.5-3" fill="none" stroke="#fff"/></svg>corporate@bramblewoodbaskets.com.au</span>
    <span><svg viewBox="0 0 16 16"><circle cx="8" cy="8" r="7" fill="none" stroke="#fff"/><circle cx="8" cy="8" r="3.5" fill="none" stroke="#fff"/><path d="M4.5 8h7M8 4.5v7" stroke="#fff"/></svg>www.bramblewoodbaskets.com.au</span>
  </footer>
</article>

<!-- Under $180 -->
<article class="page col-r row3">
  <h2 class="band">UNDER $180</h2>
  <div class="items">
    <div class="item">
      <div class="item-copy">
        <div class="item-head"><h3 class="item-name">A Cracking Verelle<br>Celebration</h3><span class="price">$149</span></div>
        <p class="item-desc">Your choice of pink or white Verelle sparkling wine 750mL, a vibrant and fresh flavour that's the perfect way to toast any occasion. Also includes tasty Australian chocolate treats - Pretzels, Berries, Scorched Almonds and Cranberries. A yummy hamper that has every taste covered! A final Christmas touch of Lumiere Crystal Christmas Bon Bon's - (Includes 2 Bon Bons containing one set of; Necklace, Earrings, Tie Clip or Cufflinks).</p>
      </div>
      <div class="photo ph-gold" role="img" aria-label="Sparkling wine with chocolates and Christmas bon bons"></div>
    </div>
    <div class="item flip">
      <div class="item-copy">
        <div class="item-head"><h3 class="item-name">Christmas with<br>Maison Verelle</h3><span class="price">$179</span></div>
        <p class="item-desc">Christmas is a time to celebrate with family &amp; friends. It's also a time for giving and saying thank you! So here are a few treats to do just that! Pop open an exquisite bottle of French Champagne, indulge in quality Australian Chocolates and crack open some Lumiere Crystal Christmas Bon Bons! (Includes 2 Bon Bons containing one set of; Necklace, Earrings, Tie Clip or Cufflinks).</p>
      </div>
      <div class="photo ph-red" role="img" aria-label="French Champagne with chocolates and bon bons"></div>
    </div>
    <div class="item">
      <div class="item-copy">
        <div class="item-head"><h3 class="item-name">White Christmas or Red<br>Christmas</h3><span class="price">$169</span></div>
        <p class="item-desc">Are you a White or Red Christmas? Simply choose your Jonah Q wine and you have the perfect seasonal hamper...you just need to add your favourite cheese. This hamper has a range of savoury delights including Cheese, Tomato &amp; Basil Artisan Crackers, Gourmet Nuts, Olives, Quince Paste, Beetroot Tapenade, Hartwell Chocolatier Hot Nuts and 2 Lumiere Bon Bons. Cheeseboard and Larchmont Cheese Knives included so you are ready to go.</p>
      </div>
      <div class="photo ph-dark" role="img" aria-label="Wine bottles with cheeseboard, crackers and savoury treats"></div>
    </div>
  </div>
  <footer class="footer">
    <span><svg viewBox="0 0 16 16"><circle cx="8" cy="8" r="7" fill="none" stroke="#fff"/><path d="M5.5 4.5l1.5 1.6-.8 1c.6 1.2 1.4 2 2.6 2.6l1-.8 1.6 1.5-.9 1.1C7.8 11.3 4.9 8.4 4.4 5.4z" fill="#fff"/></svg>1300 41 27 90</span>
    <span><svg viewBox="0 0 16 16"><circle cx="8" cy="8" r="7" fill="none" stroke="#fff"/><rect x="4.5" y="5.5" width="7" height="5" fill="none" stroke="#fff"/><path d="M4.5 5.5l3.5 3 3.5-3" fill="none" stroke="#fff"/></svg>corporate@bramblewoodbaskets.com.au</span>
    <span><svg viewBox="0 0 16 16"><circle cx="8" cy="8" r="7" fill="none" stroke="#fff"/><circle cx="8" cy="8" r="3.5" fill="none" stroke="#fff"/><path d="M4.5 8h7M8 4.5v7" stroke="#fff"/></svg>www.bramblewoodbaskets.com.au</span>
  </footer>
</article>

<!-- Under $160 (food) -->
<article class="page col-l row4">
  <h2 class="band">UNDER $160</h2>
  <div class="items">
    <div class="item">
      <div class="item-copy">
        <div class="item-head"><h3 class="item-name">Foodies Hamper</h3><span class="price">$129</span></div>
        <p class="item-desc">For the foodie in us all, here's a bit of everything from our Gourmet Hamper Range! Be it for entertaining, cooking or treating yourself, this festive season. Includes Gourmet Nuts Mix, Olive Oil, Olives, Artisan Crackers, Sundried Tomatoes, Pippa's Choc Chip Bites, Juniper &amp; Fig Choc Coffee Beans, Beetroot Marmalade, Caramelised Onions and Quince paste.</p>
      </div>
      <div class="photo ph-red" role="img" aria-label="Gourmet food hamper with oils, olives and condiments"></div>
    </div>
    <div class="item flip">
      <div class="item-copy">
        <div class="item-head"><h3 class="item-name">After Work Drinks</h3><span class="price">$129</span></div>
        <p class="item-desc">Ready, Set, Go! Everything needed for a Team gathering after work. Say thank you and celebrate what has been a tough year for so many. A gesture at Christmas shows you care. Includes Stonecrest Shiraz, Crispin Co Chipotle and Lime Tortilla Chips, Salted Cashews, Milk Chocolate Scorched Almonds, Crunchy Brittle, Pippa's handmade Choc Chip Bites, Crackers, mini Raspberry Meringues and Choc Mint Fudge.</p>
      </div>
      <div class="photo ph-dark" role="img" aria-label="Wine with chips, nuts and sweets for team drinks"></div>
    </div>
    <div class="item">
      <div class="item-copy">
        <div class="item-head"><h3 class="item-name">Good Times</h3><span class="price">$159</span></div>
        <p class="item-desc">This jam packed hamper is full of delicious goodies. Sweet, Savoury and everything tasty! Bound to be a hit when the recipient opens this box of delights. Includes Ashby's Dessert Menu Chocolates, Pretzels, Crunchy Brittle, Savoury Parmesan Paprika Cheese Bites, Chocolatier Pure Delight, mini Raspberry Meringues, Langues de Chat Matcha Green Tea Biscuits, Raspberry White Chocolate Mini Melting Moments, Buttery Shortbread, Choc Mint Fudge, Beer Nuts, and Chocolate bar.</p>
      </div>
      <div class="photo ph-gold" role="img" aria-label="Large box of sweet and savoury treats"></div>
    </div>
  </div>
  <footer class="footer">
    <span><svg viewBox="0 0 16 16"><circle cx="8" cy="8" r="7" fill="none" stroke="#fff"/><path d="M5.5 4.5l1.5 1.6-.8 1c.6 1.2 1.4 2 2.6 2.6l1-.8 1.6 1.5-.9 1.1C7.8 11.3 4.9 8.4 4.4 5.4z" fill="#fff"/></svg>1300 41 27 90</span>
    <span><svg viewBox="0 0 16 16"><circle cx="8" cy="8" r="7" fill="none" stroke="#fff"/><rect x="4.5" y="5.5" width="7" height="5" fill="none" stroke="#fff"/><path d="M4.5 5.5l3.5 3 3.5-3" fill="none" stroke="#fff"/></svg>corporate@bramblewoodbaskets.com.au</span>
    <span><svg viewBox="0 0 16 16"><circle cx="8" cy="8" r="7" fill="none" stroke="#fff"/><circle cx="8" cy="8" r="3.5" fill="none" stroke="#fff"/><path d="M4.5 8h7M8 4.5v7" stroke="#fff"/></svg>www.bramblewoodbaskets.com.au</span>
  </footer>
</article>

<!-- Luxury -->
<article class="page col-r row4">
  <h2 class="band">LUXURY</h2>
  <div class="items">
    <div class="item">
      <div class="item-copy">
        <div class="item-head"><h3 class="item-name">All Gourmet Christmas</h3><span class="price">$189</span></div>
        <p class="item-desc">When we say this is "All Gourmet" we mean it, just take a quick look at this range of delicious gourmet treats and you'll see why. Featuring beautiful quality Australian produce, sweet and savoury treats, including an exquisite bottle of boutique Ridgeway Estate Cabernet Merlot, 2 x Juniper &amp; Fig chocolates, Artisan crackers x 2, Fruit Cake, Raspberry Biscuits, Cashews, Quince Paste and 2 x Lumiere Bon Bons. This is truly a spectacular gift hamper for all who love the finer things in life.</p>
      </div>
      <div class="photo ph-red" role="img" aria-label="Luxury gourmet hamper with wine and chocolates"></div>
    </div>
    <div class="item flip">
      <div class="item-copy">
        <div class="item-head"><h3 class="item-name">A Sweet Epicurean<br>Christmas</h3><span class="price">$209</span></div>
        <p class="item-desc">A festive selection of quality chocolates and nibbles from some of Australia's premium artisan food producers. With everything from buttery shortbreads to delicious Milk Choc Delights from Juniper &amp; Fig x 3, a selection from Hartwell Chocolatier x 4, Gingerbread Reindeer, Quince Paste, Mirrabel Cacao and an Assortment from Ashby's. Add a splash of sparkle from Lumiere with 2 Crystal Bon Bons.</p>
      </div>
      <div class="photo ph-dark" role="img" aria-label="Box of premium chocolates and festive nibbles"></div>
    </div>
    <div class="item">
      <div class="item-copy">
        <div class="item-head"><h3 class="item-name">Crystal, Bubbles &amp;<br>Delicious Chocolates</h3><span class="price">$279</span></div>
        <p class="item-desc">A box of pure joy for Christmas! Recipients will be delighted by the level of luxury this hamper holds, starting with a beautiful bottle of Clos Aubrin. Also includes 4 x Hartwell Choc delights, 3 x Juniper &amp; Fig, 2 x Shortbread, crunchy Brittle, Mirrabel cacao chocolate, Ashby's dessert collection, Quince Paste and 2 Lumiere Crystal Bon Bons to crack open with Family &amp; Friends.</p>
      </div>
      <div class="photo ph-gold" role="img" aria-label="Champagne with chocolates and crystal bon bons"></div>
    </div>
  </div>
  <footer class="footer">
    <span><svg viewBox="0 0 16 16"><circle cx="8" cy="8" r="7" fill="none" stroke="#fff"/><path d="M5.5 4.5l1.5 1.6-.8 1c.6 1.2 1.4 2 2.6 2.6l1-.8 1.6 1.5-.9 1.1C7.8 11.3 4.9 8.4 4.4 5.4z" fill="#fff"/></svg>1300 41 27 90</span>
    <span><svg viewBox="0 0 16 16"><circle cx="8" cy="8" r="7" fill="none" stroke="#fff"/><rect x="4.5" y="5.5" width="7" height="5" fill="none" stroke="#fff"/><path d="M4.5 5.5l3.5 3 3.5-3" fill="none" stroke="#fff"/></svg>corporate@bramblewoodbaskets.com.au</span>
    <span><svg viewBox="0 0 16 16"><circle cx="8" cy="8" r="7" fill="none" stroke="#fff"/><circle cx="8" cy="8" r="3.5" fill="none" stroke="#fff"/><path d="M4.5 8h7M8 4.5v7" stroke="#fff"/></svg>www.bramblewoodbaskets.com.au</span>
  </footer>
</article>

<!-- Deluxe -->
<article class="page col-l row5">
  <h2 class="band">DELUXE</h2>
  <div class="items" style="bottom:auto;height:446px">
    <div class="item" style="height:240px">
      <div class="item-copy">
        <div class="item-head"><h3 class="item-name">His 'n Hers<br>Luxury Christmas</h3><span class="price">$699</span></div>
        <p class="item-desc">Our ultimate deluxe His 'n Hers Hamper! The BEST of our gourmet treats and homewares, curated for the sole purpose of everything at home in style. This incredible selection includes 2 Micro-plush Bath Robes (size M-L), 4 varieties of Hartwell Chocolates, Fernlea Aroma's Lemongrass, Lime &amp; Bergamot Kitchen Diffuser, Hand Wash and Hand Lotion, 2 x Kessler Champagne Flutes, Lune Botanica Yuzu Botanical Candle, Verda Organic Lemon Myrtle &amp; Ginger Heat Pillow, Peppermint and Rosemary Bath Soak Salts, Charcoal Face Mask, cloth and Wren &amp; Co Bath Oils and last but certainly not least, a fine bottle of Clos Aubrin to share.</p>
      </div>
      <div class="photo ph-dark" role="img" aria-label="Deluxe hamper with bath robes, candles and Champagne"></div>
    </div>
    <div class="item flip" style="height:190px">
      <div class="item-copy">
        <div class="item-head"><h3 class="item-name">The Best of<br>Everything</h3><span class="price">$869</span></div>
        <p class="item-desc">What a selection! We have put together the ultimate in gift giving, so you can say "Thank You" in a way that words can't. From the finest French Champagne to luxury Australian Chocolates and treats, to games and Premiere Lounge Movie Tickets. It's a real statement of thanks for a job very well done!</p>
      </div>
      <div class="photo ph-red" role="img" aria-label="Large deluxe hamper spread of wine, games and treats"></div>
    </div>
  </div>
  <p class="includes"><b>Includes:</b> Ashby's Chocolate Box, Crispin Co Lime &amp; Chipotle Corn Chips, Juniper &amp; Fig Chocolate Cranberries, Pretzels and Coffee Beans, Hartwell Choc Macadamias, Choc Berries, Scorched Almonds and Fruit &amp; Nut, Langues De Chat Raspberry Biscuits, Lavosh Fennel &amp; Thyme Biscuits, Pippa's Savoury Parmesan &amp; Paprika Bites, Choc Fudge Cookie Bites, Quarry Lane Coffee Espresso Blend, Saltmarsh Wine Platter Pack, Salted Cashews, Truffle Oil &amp; Salts Pack, Salted Caramel Fudge, Quince Paste, Larchmont Cheese Knives, Ashcombe Vale McLaren Vale Shiraz, Abbaye Doree, Wine Cooler Bucket, Parlour &amp; Pine Games Compendium and 2 Premiere Lounge Movie Tickets.</p>
  <footer class="footer">
    <span><svg viewBox="0 0 16 16"><circle cx="8" cy="8" r="7" fill="none" stroke="#fff"/><path d="M5.5 4.5l1.5 1.6-.8 1c.6 1.2 1.4 2 2.6 2.6l1-.8 1.6 1.5-.9 1.1C7.8 11.3 4.9 8.4 4.4 5.4z" fill="#fff"/></svg>1300 41 27 90</span>
    <span><svg viewBox="0 0 16 16"><circle cx="8" cy="8" r="7" fill="none" stroke="#fff"/><rect x="4.5" y="5.5" width="7" height="5" fill="none" stroke="#fff"/><path d="M4.5 5.5l3.5 3 3.5-3" fill="none" stroke="#fff"/></svg>corporate@bramblewoodbaskets.com.au</span>
    <span><svg viewBox="0 0 16 16"><circle cx="8" cy="8" r="7" fill="none" stroke="#fff"/><circle cx="8" cy="8" r="3.5" fill="none" stroke="#fff"/><path d="M4.5 8h7M8 4.5v7" stroke="#fff"/></svg>www.bramblewoodbaskets.com.au</span>
  </footer>
</article>

<!-- How to order -->
<article class="page col-r row5 order">
  <div class="sheet">
    <section>
      <h3>How to Order your Corporate Gifts</h3>
      <p><b>Follow these simple steps to order</b></p>
      <ul>
        <li>Go to bramblewoodbaskets.com.au to download the Bulk Order Form</li>
        <li>Complete and email to corporate@bramblewoodbaskets.com.au</li>
        <li>Payment must be made before we can prepare your order as we pack most hampers the same day or pre-pack and store for sending on the day of your choice.</li>
      </ul>
      <p>Please allow 2-3 days for your order to be prepared and dispatched. For orders of 50 hampers or more, and depending on stock levels, we are able to customise hampers as a special service. Just email us at corporate@bramblewoodbaskets.com.au</p>
    </section>
    <section>
      <h3>Delivery &amp; Shipping Fees</h3>
      <p>All bulk orders receive FREE Standard Shipping around Australia with an estimated 2-5 business days delivery to all major cities. Our Premium 1 - 2 business day delivery option is $9.95 per hamper for individual parcels going to individual metro addresses. Premium Shipping for multiple hampers going to one address varies depending on the quantity.</p>
      <p>With the impact of Covid 19, and increased online shopping, we expect delivery times this Christmas to be longer than usual, so please plan ahead. Rest assured we try as hard as we can to ensure your order arrives as requested but please understand once orders leave our warehouse, delivery is in the hands of the shipping company.</p>
      <p>Note: Any mistakes made on the bulk order form (address, company names etc) may result in the parcel being returned to our warehouse and a redelivery fee being applied.</p>
    </section>
    <section>
      <h3>What our Customers have Said</h3>
      <div class="quote">I would like to say a massive thank you. Your service is fantastic and the staff member I spoke to on the phone was just wonderful. On such a busy day and considering I put a late order in. The hamper has been delivered and you really made someone's day. Thank you Thankyou<cite>— Dana</cite></div>
      <div class="quote">I ordered a hamper yesterday midmorning for a dear friend and it was delivered on the same day! I know sometimes it is not possible but I was pleasantly surprised by it. Keep up the good work, I will recommend you whenever I hear someone is looking for an extraordinary hamper.<cite>— Noel</cite></div>
    </section>
  </div>
  <footer class="footer">
    <span><svg viewBox="0 0 16 16"><circle cx="8" cy="8" r="7" fill="none" stroke="#fff"/><path d="M5.5 4.5l1.5 1.6-.8 1c.6 1.2 1.4 2 2.6 2.6l1-.8 1.6 1.5-.9 1.1C7.8 11.3 4.9 8.4 4.4 5.4z" fill="#fff"/></svg>1300 41 27 90</span>
    <span><svg viewBox="0 0 16 16"><circle cx="8" cy="8" r="7" fill="none" stroke="#fff"/><rect x="4.5" y="5.5" width="7" height="5" fill="none" stroke="#fff"/><path d="M4.5 5.5l3.5 3 3.5-3" fill="none" stroke="#fff"/></svg>corporate@bramblewoodbaskets.com.au</span>
    <span><svg viewBox="0 0 16 16"><circle cx="8" cy="8" r="7" fill="none" stroke="#fff"/><circle cx="8" cy="8" r="3.5" fill="none" stroke="#fff"/><path d="M4.5 8h7M8 4.5v7" stroke="#fff"/></svg>www.bramblewoodbaskets.com.au</span>
  </footer>
</article>

<!-- Customise -->
<article class="page col-c row6 custom">
  <div class="sheet">
    <div class="split">
      <div>
        <h3>Customise with your own<br>Corporate Ribbon</h3>
        <p>All of our Corporate Hampers can be personalised and branded with your company ribbon. This is a lovely added touch to give more impact for your brand. Simply request your corporate ribbon on our bulk order form and include your company logo and we will do the rest.</p>
        <p style="margin-top:6px">Your logo can be printed in Gold or Silver on satin ribbon and is $4.95 per hamper.</p>
      </div>
      <div class="photo ph-red" role="img" aria-label="Red satin ribbon printed with a company logo"></div>
    </div>
    <div class="split">
      <div>
        <h3>Free Gift Card</h3>
        <p>All Hampers include a free Christmas Gift Card with your own personalised message, if you so wish.</p>
      </div>
      <div class="photo ph-red" style="height:130px" role="img" aria-label="Red Christmas gift card with white pattern"></div>
    </div>
    <section>
      <h3>Our Suppliers</h3>
      <p>Our beautiful Hampers are curated using only the best products and we are proud to be working with these quality brands.</p>
      <div class="suppliers">
        <div class="badge" role="img" aria-label="Supplier badge"></div>
        <div class="badge" role="img" aria-label="Supplier badge"></div>
        <div class="badge" role="img" aria-label="Supplier badge"></div>
        <div class="badge" role="img" aria-label="Supplier badge"></div>
        <div class="badge" role="img" aria-label="Supplier badge"></div>
        <div class="badge" role="img" aria-label="Supplier badge"></div>
        <div class="badge" role="img" aria-label="Supplier badge"></div>
        <div class="badge" role="img" aria-label="Supplier badge"></div>
        <div class="badge last" role="img" aria-label="Supplier badge"></div>
      </div>
    </section>
  </div>
  <footer class="footer">
    <span><svg viewBox="0 0 16 16"><circle cx="8" cy="8" r="7" fill="none" stroke="#fff"/><path d="M5.5 4.5l1.5 1.6-.8 1c.6 1.2 1.4 2 2.6 2.6l1-.8 1.6 1.5-.9 1.1C7.8 11.3 4.9 8.4 4.4 5.4z" fill="#fff"/></svg>1300 41 27 90</span>
    <span><svg viewBox="0 0 16 16"><circle cx="8" cy="8" r="7" fill="none" stroke="#fff"/><rect x="4.5" y="5.5" width="7" height="5" fill="none" stroke="#fff"/><path d="M4.5 5.5l3.5 3 3.5-3" fill="none" stroke="#fff"/></svg>corporate@bramblewoodbaskets.com.au</span>
    <span><svg viewBox="0 0 16 16"><circle cx="8" cy="8" r="7" fill="none" stroke="#fff"/><circle cx="8" cy="8" r="3.5" fill="none" stroke="#fff"/><path d="M4.5 8h7M8 4.5v7" stroke="#fff"/></svg>www.bramblewoodbaskets.com.au</span>
  </footer>
</article>

</body>
</html>
```